Biz Cards for Lumivale Associates

Lumivale Associates is seeking a single-sided business card that is more visually-appealing than our current design (see attached).

Notes:
- Our colors are blue & teal.
- Our tag line must be large enough to be easily read
- We don't necessarily need our address included (that's just the biz office)
- We'd like to add our email address: Lumivale512@brindlemail.net

Thanks!

Industry/Entity Type

Business

Contact Information for Business Card

Standard size
PSD file required w/ text on its own layer

Colors
86cfc6
3277b5

```html
<!DOCTYPE html>
<html lang="en">
<head>
<meta charset="utf-8">
<title>Lumivale Associates – Business Card</title>
<link rel="stylesheet" href="https://fonts.googleapis.com/css2?family=Cinzel:wght@400;600&family=Roboto+Condensed:wght@500&family=Roboto:wght@400&display=swap">
<style>
  :root {
    --backdrop: #3b3b3d;
    --card: #232325;
    --card-edge: #1a1a1b;
    --emboss: #6a6a6d;
    --white: #f1f1f1;
    --silver: #c8c8c8;
    --teal: #1fb3a3;
    --teal-soft: #86cfc6;
    --blue: #3277b5;
  }
  * { box-sizing: border-box; margin: 0; padding: 0; }
  html, body { width: 799px; height: 1200px; overflow: hidden; }
  body {
    background: var(--backdrop);
    position: relative;
    font-family: "Roboto", Arial, sans-serif;
  }
  .card {
    position: absolute;
    left: 80px;
    width: 640px;
    height: 366px;
    background: var(--card);
    border: 1px solid var(--card-edge);
    overflow: hidden;
    box-shadow: 0 14px 30px rgba(0,0,0,.45);
  }
  .card--front { top: 150px; }
  .card--back { top: 684px; }

  /* Front */
  .front-mark {
    position: absolute;
    left: 220px; top: 83px;
    width: 200px; height: 200px;
    border: 3px solid var(--emboss);
    border-radius: 50%;
    display: flex; align-items: center; justify-content: center;
    text-align: center;
  }
  .front-mark__name {
    font-family: "Cinzel", Georgia, serif;
    font-weight: 600;
    font-size: 19px;
    line-height: 1.3;
    letter-spacing: 1px;
    color: var(--emboss);
  }

  /* Back */
  .wordmark {
    position: absolute;
    left: 34px; top: 30px;
    font-family: "Cinzel", Georgia, serif;
    font-weight: 600;
    color: var(--white);
    line-height: 1;
  }
  .wordmark__main { font-size: 40px; letter-spacing: 1px; }
  .wordmark__sub { font-size: 17px; letter-spacing: 7px; margin-top: 4px; padding-left: 4px; }

  .person { position: absolute; left: 34px; top: 140px; }
  .person__name {
    font-family: "Roboto Condensed", Arial Narrow, sans-serif;
    font-weight: 500;
    font-size: 23px;
    color: var(--teal);
  }
  .person__title { font-size: 13px; color: var(--silver); margin-top: 2px; }

  .contacts { position: absolute; left: 34px; top: 210px; list-style: none; }
  .contacts li {
    display: flex; align-items: center; gap: 10px;
    font-size: 14px; color: var(--white);
    height: 22px;
  }
  .contacts svg { width: 13px; height: 13px; fill: var(--teal); flex: none; }
  .contacts .accent { color: var(--teal); }

  .back-mark {
    position: absolute;
    left: 390px; top: 150px;
    width: 330px; height: 330px;
    border: 5px solid var(--silver);
    border-radius: 50%;
  }
  .back-mark__name {
    position: absolute;
    left: 420px; top: 250px;
    width: 220px;
    text-align: center;
    font-family: "Cinzel", Georgia, serif;
    font-weight: 600;
    font-size: 24px;
    line-height: 1.25;
    color: var(--teal-soft);
  }
</style>
</head>
<body>

<section class="card card--front" aria-label="Card front">
  <div class="front-mark">
    <p class="front-mark__name">Lumivale<br>Associates</p>
  </div>
</section>

<section class="card card--back" aria-label="Card back">
  <div class="wordmark">
    <p class="wordmark__main">LUMIVALE</p>
    <p class="wordmark__sub">ASSOCIATES Ltd</p>
  </div>

  <div class="person">
    <p class="person__name">Maren Castell, RN</p>
    <p class="person__title">Mental Health Therapist</p>
  </div>

  <ul class="contacts">
    <li><svg viewBox="0 0 16 16" aria-hidden="true"><path d="M3 1h3l1 4-2 1a9 9 0 0 0 5 5l1-2 4 1v3c0 1-1 2-2 2A13 13 0 0 1 1 3c0-1 1-2 2-2z"/></svg>(855) LUMI-VAL</li>
    <li><svg viewBox="0 0 16 16" aria-hidden="true"><path d="M3 1h3l1 4-2 1a9 9 0 0 0 5 5l1-2 4 1v3c0 1-1 2-2 2A13 13 0 0 1 1 3c0-1 1-2 2-2z"/></svg>(330) 555-0184</li>
    <li><svg viewBox="0 0 16 16" aria-hidden="true"><path d="M8 1a7 7 0 1 0 0 14A7 7 0 0 0 8 1zm0 1.5c.9 1.2 1.5 2.8 1.6 4.5H6.4C6.5 5.3 7.1 3.7 8 2.5zM2.6 7.1h2.3c.1 1.8.6 3.4 1.4 4.7A5.6 5.6 0 0 1 2.6 7.1zm6.7 0h-2.6V9h2.6zm1.8 0h2.3a5.6 5.6 0 0 1-3.7 4.7c.8-1.3 1.3-2.9 1.4-4.7z"/></svg><span>www.<span class="accent">Lumivale</span>.net</span></li>
    <li><svg viewBox="0 0 16 16" aria-hidden="true"><path d="M1 3h14v10H1zm1.5 1.5v.3L8 9l5.5-4.2v-.3zm0 2.2v4.8h11V6.7L8 11z"/></svg>Lumivale512@brindlemail.net</li>
  </ul>

  <div class="back-mark" aria-hidden="true"></div>
  <p class="back-mark__name">Lumivale<br>Associates</p>
</section>

</body>
</html>
```